Glint5Gate Photography Business Cards

We need a good general business card that we can hand to our clients. We will be doing embossed gloss cards.

Target Market(s)

Real estate / Business to business / professionals

```html
<!DOCTYPE html>
<html lang="en">
<head>
<meta charset="utf-8">
<title>Glint5Gate Photography – Business Card</title>
<link href="https://fonts.googleapis.com/css2?family=Open+Sans:wght@400;700&display=swap" rel="stylesheet">
<style>
  :root {
    --stage: #1f1f21;
    --paper: #ffffff;
    --navy: #2a2168;
    --navy-soft: #332a78;
    --sky: #2a9fe0;
    --ink: #2b2b2b;
    --rule: #9a9a9a;
  }
  * { margin: 0; padding: 0; box-sizing: border-box; }
  html, body {
    width: 1200px; height: 1108px; overflow: hidden;
    background: var(--stage);
    font-family: "Open Sans", Arial, sans-serif;
  }
  .card-set {
    position: relative; width: 1200px; height: 1108px;
  }
  .card {
    position: absolute; top: 204px; width: 420px; height: 700px;
    border-radius: 22px; overflow: hidden;
  }
  .card-front { left: 150px; background: var(--paper); }
  .card-back { left: 630px; background: var(--navy); }

  /* Front */
  .brand-name {
    position: absolute; top: 150px; left: 0; right: 0;
    text-align: center; color: var(--navy);
    font-weight: 700; font-size: 40px; line-height: 1.1;
  }
  .brand-name span { display: block; }
  .person {
    position: absolute; top: 360px; left: 0; right: 0; text-align: center;
  }
  .person-name { color: var(--navy); font-weight: 700; font-size: 27px; }
  .person-title {
    color: var(--sky); font-size: 18px; letter-spacing: 0.5px; margin-top: 2px;
  }
  .icon-row {
    position: absolute; top: 452px; left: 40px; right: 40px;
    display: flex; align-items: center; gap: 8px;
  }
  .icon-row .rule { flex: 1; height: 1px; background: var(--rule); }
  .icon-tile {
    width: 34px; height: 34px; border-radius: 5px; background: var(--navy);
    display: flex; align-items: center; justify-content: center;
  }
  .contact-list {
    position: absolute; top: 506px; left: 0; right: 0; text-align: center;
    color: var(--ink); font-size: 17px; line-height: 27px; list-style: none;
  }
  .contact-list .accent { color: var(--sky); }
  .address-rule {
    position: absolute; top: 624px; left: 70px; right: 70px;
    height: 1px; background: var(--rule);
  }
  .address {
    position: absolute; top: 636px; left: 0; right: 0; text-align: center;
    color: var(--ink); font-size: 17px; line-height: 25px; font-style: normal;
  }

  /* Back */
  .pattern-field {
    position: absolute; inset: 0;
    background: radial-gradient(ellipse at 70% 30%, var(--navy-soft) 0%, var(--navy) 70%);
  }
  .back-mark {
    position: absolute; left: 210px; top: 480px; width: 180px;
    display: flex; flex-direction: column; align-items: center; gap: 10px;
  }
  .back-mark .dot {
    width: 46px; height: 46px; border-radius: 50%; border: 3px solid var(--paper);
  }
  .back-mark .name {
    color: var(--paper); font-weight: 700; font-size: 17px; text-align: center; line-height: 1.2;
  }
</style>
</head>
<body>
<main class="card-set">
  <section class="card card-front" aria-label="Card front">
    <h1 class="brand-name"><span>Glint5Gate</span><span>Photography</span></h1>

    <div class="person">
      <p class="person-name">Marcus Hale</p>
      <p class="person-title">MANAGING DIRECTOR</p>
    </div>

    <div class="icon-row">
      <span class="rule"></span>
      <span class="icon-tile" aria-label="Phone">
        <svg width="20" height="20" viewBox="0 0 20 20"><path d="M4 3h4l1 4-2 1.5a10 10 0 0 0 4.5 4.5L13 11l4 1v4a2 2 0 0 1-2 2A13 13 0 0 1 2 5a2 2 0 0 1 2-2z" fill="#fff"/></svg>
      </span>
      <span class="icon-tile" aria-label="Mobile">
        <svg width="20" height="20" viewBox="0 0 20 20"><rect x="5" y="2" width="10" height="16" rx="2" fill="none" stroke="#fff" stroke-width="2"/><circle cx="10" cy="15" r="1" fill="#fff"/></svg>
      </span>
      <span class="icon-tile" aria-label="Email">
        <svg width="20" height="20" viewBox="0 0 20 20"><rect x="2" y="4" width="16" height="12" fill="none" stroke="#fff" stroke-width="2"/><path d="M2 4l8 7 8-7" fill="none" stroke="#fff" stroke-width="2"/></svg>
      </span>
      <span class="icon-tile" aria-label="Website">
        <svg width="20" height="20" viewBox="0 0 20 20"><circle cx="10" cy="10" r="7.5" fill="none" stroke="#fff" stroke-width="2"/><path d="M2.5 10h15M10 2.5c3 3 3 12 0 15M10 2.5c-3 3-3 12 0 15" fill="none" stroke="#fff" stroke-width="1.5"/></svg>
      </span>
      <span class="rule"></span>
    </div>

    <ul class="contact-list">
      <li>044-310 275 864</li>
      <li>044-310 275 864</li>
      <li>hello@glintgate.com</li>
      <li>www.<span class="accent">glintgate</span>.com</li>
    </ul>

    <div class="address-rule"></div>
    <address class="address">58, Harbor Lane<br>20314, Country Name</address>
  </section>

  <section class="card card-back" aria-label="Card back">
    <div class="pattern-field" role="img" aria-label="Faint repeating brand badge pattern in muted navy"></div>
    <div class="back-mark">
      <span class="dot"></span>
      <span class="name">Glint5Gate Photography</span>
    </div>
  </section>
</main>
</body>
</html>
```